Verantix - Solution provider in business consulting

Verantix is a swiss based company providing solutions for developing markets. The business covers various fields of business consulting, such as supply chain, product costs, quality management and manufacturing management. The Business operates in a efficient, straight and solution oriented manner.
The final design should communicate these characteristics. Asian people as well as as western people shall identify the qualities of the company at first sight.
The customer needs business cards with a simple view but an recognizable design, printed in high quality. Engraved elements such as the globe or simple words are possible.
Available colors are: (RAL)
102/102/102
51/102/102
153/204/153
255/102/51
Font: Calibri
Industry/Entity Type
Business
Look and feel
Each slider illustrates characteristics of the customer's brand and the style your logo design should communicate.

```html
<!DOCTYPE html>
<html lang="en">
<head>
<meta charset="utf-8">
<title>Verantix – Business Card</title>
<link href="https://fonts.googleapis.com/css2?family=Carlito:wght@400;700&display=swap" rel="stylesheet">
<style>
  :root {
    --page-bg: #dfe4ea;
    --card-bg: #f3f4f5;
    --ink: #4a4a4a;
    --ink-soft: #5c5c5c;
    --band-bg: #4d4f50;
    --band-ink: #d4d8dc;
    --rule: #4a4a4a;
  }
  * { margin: 0; padding: 0; box-sizing: border-box; }
  html, body {
    width: 1200px; height: 980px; overflow: hidden;
    background: var(--page-bg);
    font-family: "Carlito", "Calibri", sans-serif;
  }
  .card {
    position: absolute; left: 100px; top: 183px;
    width: 1000px; height: 614px;
    background: var(--card-bg);
    overflow: hidden;
    box-shadow: 0 6px 24px rgba(0,0,0,0.12);
  }
  .brand {
    position: absolute; left: 0; right: 0; top: 80px;
    display: flex; justify-content: center; align-items: center; gap: 18px;
    color: var(--ink);
  }
  .brand-name { font-size: 68px; font-weight: 400; letter-spacing: 1px; }
  .brand-dot { width: 26px; height: 26px; border-radius: 50%; background: var(--ink); }
  .name-row {
    position: absolute; left: 0; right: 0; top: 260px;
    display: flex; align-items: center;
  }
  .name-row .rule-short { width: 43px; height: 3px; background: var(--rule); }
  .name-row .rule-long { flex: 1; height: 3px; background: var(--rule); }
  .person-name {
    font-size: 33px; font-weight: 700; color: var(--ink-soft);
    letter-spacing: 0.5px; padding: 0 14px;
  }
  .person-role {
    position: absolute; left: 57px; top: 300px;
    font-size: 24px; color: var(--ink);
  }
  .contacts { position: absolute; left: 66px; top: 354px; list-style: none; }
  .contacts li {
    display: flex; align-items: center; height: 36px;
    font-size: 26px; color: var(--ink);
  }
  .contacts svg { width: 24px; height: 24px; margin-right: 20px; fill: var(--ink); }
  .footer-band {
    position: absolute; left: 0; right: 0; bottom: 0; height: 100px;
    background: var(--band-bg); color: var(--band-ink);
    padding: 14px 0 0 55px;
  }
  .company { font-size: 26px; font-weight: 700; }
  .address { font-size: 26px; margin-top: 4px; }
  .deco-circle {
    position: absolute; left: 722px; top: 446px;
    width: 146px; height: 146px; border-radius: 50%;
    border: 3px solid var(--band-ink); opacity: 0.55;
  }
</style>
</head>
<body>
  <main class="card">
    <div class="brand">
      <span class="brand-name">verantix</span>
      <span class="brand-dot"></span>
    </div>

    <div class="name-row">
      <span class="rule-short"></span>
      <span class="person-name">MARCO KELLER</span>
      <span class="rule-long"></span>
    </div>
    <div class="person-role">CEO</div>

    <ul class="contacts">
      <li>
        <svg viewBox="0 0 24 24" aria-hidden="true"><rect x="0" y="0" width="24" height="24" rx="4"/><path d="M7 5c1 0 2 3 2 4s-1 1-1 2 3 4 4 4 1-1 2-1 4 1 4 2-1 3-3 3C10 19 5 14 5 8c0-2 1-3 2-3z" fill="#f3f4f5"/></svg>
        +41 79 555 0182
      </li>
      <li>
        <svg viewBox="0 0 24 24" aria-hidden="true"><rect x="0" y="0" width="24" height="24" rx="4"/><rect x="7" y="4" width="10" height="6" fill="#f3f4f5"/><rect x="4" y="11" width="16" height="6" fill="#f3f4f5"/><rect x="7" y="15" width="10" height="5" fill="#f3f4f5"/></svg>
        +41 71 555 0347
      </li>
      <li>
        <svg viewBox="0 0 24 24" aria-hidden="true"><rect x="0" y="0" width="24" height="24" rx="4"/><rect x="4" y="7" width="16" height="11" fill="#f3f4f5"/><path d="M4 7l8 6 8-6" fill="none" stroke="#4a4a4a" stroke-width="2"/></svg>
        marco.keller@verantix.ch
      </li>
      <li>
        <svg viewBox="0 0 24 24" aria-hidden="true"><rect x="0" y="0" width="24" height="24" rx="4"/><circle cx="12" cy="12" r="7" fill="none" stroke="#f3f4f5" stroke-width="2"/><path d="M5 12h14M12 5c-3 4-3 10 0 14M12 5c3 4 3 10 0 14" fill="none" stroke="#f3f4f5" stroke-width="1.5"/></svg>
        www.verantix.ch
      </li>
    </ul>

    <footer class="footer-band">
      <div class="company">Verantix GmbH</div>
      <div class="address">Feldstrasse 12, 8572 Brunnau, Switzerland</div>
    </footer>
    <div class="deco-circle" aria-hidden="true"></div>
  </main>
</body>
</html>
```